Eye-catching Yellow Page Ad for Attorney's Office

We need a phone book advertisement for our law office. We practice workers' compensation law, and our clientele consists exclusively of individuals who have been injured on the job. The dimensions of the print ad will be 6" W X 4.54" H.

We've had our current ad for several years, and wanted to get a new one that has been designed by a professional. Being that it's an ad for a law firm, it needs to be professional looking, but we're hoping to have something that looks a little more modern and has eye-catching appeal. We like the text that is included in the ad, and we want to make sure our phone number is very visible. No real preference for color scheme.

I've attached a copy of our current ad. All the information included in there is accurate. Our office name is Thornbury & Lisle, PLLC. The ethical rules for attorney advertising require the PLLC to be included in the ad, but it can be smaller than the other text (see our current ad).

Target Market(s)

Our potential clients are injured workers looking for legal representation in their workers' compensation claim.

Industry/Entity Type

Attorney

Font styles to use
Serif
Sans Serif

Requirements
Must have
• Professional, but stands out from the crowd
Nice to have
• Clean modern design
Should not have
• We don't want it to be too crowded or over-worked.

```html
<!DOCTYPE html>
<html lang="en">
<head>
<meta charset="utf-8">
<title>Thornbury &amp; Lisle — Workers Compensation</title>
<link href="https://fonts.googleapis.com/css2?family=Arimo:wght@400;700&display=swap" rel="stylesheet">
<style>
  :root {
    --ink: #000000;
    --headline-yellow: #ffff00;
    --paper: #ffffff;
    --panel-orange: rgba(226, 132, 72, 0.82);
    --callout-orange: rgba(196, 92, 20, 0.85);
    --sky-top: #8fa6bf;
    --sky-mid: #c9b7a4;
    --sky-glow: #f3b860;
    --ground: #2a1a10;
  }
  * { margin: 0; padding: 0; box-sizing: border-box; }
  html, body { width: 1200px; height: 909px; overflow: hidden; background: var(--paper); }
  body { font-family: "Arimo", Arial, sans-serif; }

  .ad { position: relative; width: 1200px; height: 909px; background: var(--paper); overflow: hidden; }

  .masthead {
    position: absolute; left: 0; top: 0; width: 1200px; height: 166px;
    background: var(--ink); text-align: center;
  }
  .firm-name {
    color: var(--headline-yellow); font-weight: 700; font-size: 100px;
    line-height: 1; padding-top: 14px; letter-spacing: -1px;
  }
  .tagline {
    color: var(--paper); font-weight: 700; font-size: 28px; letter-spacing: 9.5px;
    margin-top: 14px; white-space: nowrap;
  }

  .scene {
    position: absolute; left: 3px; top: 166px; width: 1197px; height: 740px;
    background:
      radial-gradient(ellipse 520px 300px at 1000px 640px, var(--sky-glow), transparent 70%),
      linear-gradient(180deg, var(--sky-top) 0%, #a9b4c0 40%, var(--sky-mid) 70%, #e0a060 88%, var(--ground) 100%);
  }

  .services-panel {
    position: absolute; left: 3px; top: 166px; width: 642px; height: 740px;
    background: var(--panel-orange);
  }
  .practice-title {
    position: absolute; left: 85px; top: 232px; color: var(--paper);
    font-weight: 700; font-size: 56px; line-height: 0.97;
  }
  .help-band {
    position: absolute; left: 0; top: 360px; width: 576px; height: 74px;
    background: var(--ink); color: var(--paper); font-weight: 700; font-size: 42px;
    line-height: 74px; padding-left: 93px;
  }
  .service-list {
    position: absolute; left: 102px; top: 452px; list-style: none;
    color: var(--ink); font-size: 22px; line-height: 28px;
  }
  .phone {
    position: absolute; left: 97px; top: 696px; color: var(--paper);
    font-weight: 700; font-size: 67px; line-height: 1;
  }
  .legal-name {
    position: absolute; left: 99px; top: 782px; color: var(--ink);
    font-weight: 700; font-size: 26px;
  }
  .address {
    position: absolute; left: 99px; top: 818px; color: var(--ink); font-size: 16px;
  }

  .credential-callout {
    position: absolute; left: 835px; top: 465px; width: 365px; height: 118px;
    background: var(--callout-orange); color: var(--paper);
    font-size: 16px; line-height: 19px; padding: 18px 0 0 20px;
  }
</style>
</head>
<body>
  <main class="ad">
    <header class="masthead">
      <h1 class="firm-name">Thornbury &amp; Lisle</h1>
      <p class="tagline">PROFESSIONAL . COMMITTED .&nbsp; EFFECTIVE</p>
    </header>

    <div class="scene" role="img" aria-label="Photograph of an injured worker on crutches silhouetted against a sunset sky"></div>

    <section class="services-panel" aria-hidden="false"></section>
    <h2 class="practice-title">Workers<br>Compensation</h2>
    <div class="help-band">We can help with :</div>
    <ul class="service-list">
      <li>Workforce Injuries or Death</li>
      <li>Lost Wages</li>
      <li>Hearing Loss Claims</li>
      <li>Pension Claims</li>
      <li>Disability awards</li>
      <li>Return to work Issues</li>
      <li>Medical Expenses &amp; Treatment</li>
    </ul>
    <p class="phone">360-555-0142</p>
    <p class="legal-name">Thornbury &amp; Lisle, PLLC</p>
    <p class="address">48 N. Harbor Street, Suite 410, Fairhaven, WA 98226</p>

    <aside class="credential-callout">
      Former Assistant Attorney’s General<br>
      who Knows the System that means<br>
      Case will be handled by an Attorney<br>
      rather than assistant
    </aside>
  </main>
</body>
</html>
```